QRV Consulting Web Design… We need a Facelift!

We currently have a website but it is very outdated. We like our content, but could use some help on giving it a refreshed facelift.

www.QRV-Consulting.example is our site

We only consult with large companies in the US that have sales over $250,000 a year, so looking to be high end yet approachable in our look.

Target Market(s)

Large corporations

Industry/Entity Type

Consulting

Coding

Coded - Design and coding required

Number of Pages Required

5+ page

Font styles to use
Serif
Sans Serif

Requirements
Must have
• We love our logo, keep that the same.
• The site colors can deviate from the logo, as long as it is complimentary
Nice to have
• We like our videos and graphics. If you can make them better, then great! But you can also feel free to reuse them.
• There is a video on the opening screen and one on the video page.
• We would like the video on the video page to be incorporated on the first page.
• If you think we need other/more page, we are all ears!
Should not have
• Want to set us apart from our competition in look, feel, professionalism and step away from the old fashioned conservatives of their websites. We want to be professional, yet bolder and fresher.
• Our Competition is LedgerPilot.example and TheBrindlewoodGroup.example, but not looking to copy of emulate them, but gives an idea of the world QRV is in.

```html
<!DOCTYPE html>
<html lang="en">
<head>
<meta charset="utf-8">
<title>QRV Consulting</title>
<link rel="stylesheet" href="https://fonts.googleapis.com/css2?family=Open+Sans:wght@400;600;700&display=swap">
<style>
:root{
  --red:#c4161c;
  --navy:#1d3f7a;
  --ink:#333;
  --muted:#777;
  --band:#ececec;
  --line:#dcdcdc;
  --white:#fff;
}
*{box-sizing:border-box;margin:0;padding:0}
html,body{width:1200px;height:2568px;overflow:hidden}
body{position:relative;background:var(--white);font-family:"Open Sans",Arial,sans-serif;color:var(--ink)}

/* header */
.site-header{position:absolute;left:0;top:0;width:1200px;height:110px;background:var(--white)}
.brand{position:absolute;left:50px;top:36px;display:flex;align-items:center;gap:10px}
.brand-dot{width:34px;height:34px;border-radius:50%;background:var(--navy)}
.brand-name{font-size:20px;font-weight:700;color:var(--navy)}
.topbar{position:absolute;right:60px;top:26px;display:flex;align-items:center;gap:7px;font-size:12px;font-weight:600;color:var(--ink)}
.topbar .call{margin-right:12px;display:flex;align-items:center;gap:6px}
.dot-icon{width:18px;height:18px;border-radius:50%;background:var(--navy)}
.dot-icon.red{background:var(--red)}
.main-nav{position:absolute;left:460px;top:64px;display:flex}
.main-nav a{display:block;width:110px;padding:8px 0;text-align:center;font-size:11px;font-weight:600;color:var(--ink);text-decoration:none;text-transform:uppercase;border-right:1px solid var(--line)}
.main-nav a.active{background:var(--red);color:var(--white)}

/* hero */
.hero-band{position:absolute;left:0;top:110px;width:1200px;height:490px;background:var(--band)}
.hero-slide{position:absolute;left:110px;top:118px;width:1000px;height:452px;background:linear-gradient(135deg,#4d5866 0%,#c9ccc8 30%,#efeee9 50%,#b8bcc0 70%,#3e4753 100%);border:5px solid #7d8fb4}
.hero-caption{position:absolute;left:115px;top:265px;width:350px;padding:12px 16px;background:rgba(255,255,255,.85);color:var(--red);font-size:26px;font-weight:600;line-height:1.15}
.slider-dots{position:absolute;left:0;width:1200px;top:582px;display:flex;justify-content:center;gap:8px}
.slider-dots span{width:8px;height:8px;border-radius:50%;background:#aaa}
.slider-dots span.on{background:var(--red)}

/* headings */
.section-title{position:absolute;left:0;width:1200px;text-align:center;font-size:32px;font-weight:400;color:#222;line-height:1.2}
.section-title em{font-style:normal;color:var(--red)}
.title-rule{position:absolute;left:560px;width:80px;height:3px;background:var(--red)}

/* welcome */
.welcome-text{position:absolute;left:110px;top:722px;width:980px;font-size:11px;line-height:1.9;color:var(--muted);text-align:center}
.btn{position:absolute;display:flex;align-items:center;justify-content:center;background:var(--red);color:var(--white);font-size:11px;font-weight:600}

/* why */
.why-band{position:absolute;left:0;top:920px;width:1200px;height:420px;background:var(--band)}
.why-card{position:absolute;top:1030px;width:280px}
.why-photo{width:280px;height:140px}
.why-card h3{margin-top:12px;font-size:16px;font-weight:700;color:#222}
.why-card .bar{width:280px;height:2px;background:var(--red);margin:4px 0 6px}
.why-card p{font-size:10px;line-height:1.6;color:var(--muted)}
.arrow-btn{position:absolute;top:1134px;width:24px;height:24px;border-radius:50%;background:#222;display:flex;align-items:center;justify-content:center}

/* video */
.video-band{position:absolute;left:0;top:1340px;width:1200px;height:320px;background:linear-gradient(110deg,#2f343b 0%,#6a6f76 35%,#3d424a 60%,#1f2226 100%)}
.play{position:absolute;left:570px;top:1450px;width:60px;height:60px;border-radius:50%;border:3px solid var(--white);display:flex;align-items:center;justify-content:center}
.video-label{position:absolute;left:0;width:1200px;top:1520px;text-align:center;font-size:10px;color:#ddd}

/* process */
.step{position:absolute;top:1790px;width:250px;text-align:center}
.step-ring{margin:0 auto;width:124px;height:124px;border-radius:50%;border:6px solid var(--red);box-shadow:0 0 0 5px var(--navy);display:flex;align-items:center;justify-content:center;background:var(--white)}
.step h3{margin-top:22px;font-size:17px;font-weight:600;color:var(--red)}
.step p{margin-top:4px;font-size:10px;line-height:1.5;color:var(--muted)}
.step-arrow{position:absolute;top:1838px}

/* contact */
.contact-band{position:absolute;left:0;top:2030px;width:1200px;height:440px;background:linear-gradient(180deg,#2a2d31,#17191c)}
.contact-title{color:var(--white)}
.contact-info{position:absolute;left:170px;top:2240px;font-size:11px;color:#ddd;line-height:1.5}
.contact-info li{list-style:none;display:flex;gap:10px;align-items:flex-start;margin-bottom:40px;width:330px}
.contact-form{position:absolute;left:620px;top:2225px;width:250px}
.field{height:22px;margin-bottom:14px;border-bottom:1px solid #555;font-size:9px;color:#999;padding-left:4px}
.field.msg{height:50px}
.submit{width:80px;height:22px;background:#3d6fc4;color:var(--white);font-size:9px;display:flex;align-items:center;justify-content:center;margin:14px 0 0 85px}

/* footer */
.site-footer{position:absolute;left:0;top:2470px;width:1200px;height:98px;background:var(--white)}
.footer-links{position:absolute;left:100px;top:28px;font-size:10px;color:var(--ink)}
.copyright{position:absolute;left:100px;top:46px;font-size:9px;color:var(--muted)}
.follow{position:absolute;right:110px;top:40px;display:flex;gap:6px;align-items:center;font-size:15px;font-weight:600;color:var(--ink)}
.follow .dot-icon{width:22px;height:22px}
</style>
</head>
<body>

<header class="site-header">
  <div class="brand">
    <span class="brand-dot"></span>
    <span class="brand-name">QRV Consulting</span>
  </div>
  <div class="topbar">
    <span class="call">
      <svg width="14" height="14" viewBox="0 0 24 24"><path fill="#c4161c" d="M6.6 10.8a15 15 0 0 0 6.6 6.6l2.2-2.2c.3-.3.7-.4 1-.2 1.1.4 2.3.6 3.6.6.6 0 1 .4 1 1V20c0 .6-.4 1-1 1A17 17 0 0 1 3 4c0-.6.4-1 1-1h3.5c.6 0 1 .4 1 1 0 1.3.2 2.5.6 3.6.1.3 0 .7-.2 1z"/></svg>
      CALL US NOW: (555) 014-2780
    </span>
    <span class="dot-icon"></span><span class="dot-icon red"></span><span class="dot-icon"></span><span class="dot-icon red"></span><span class="dot-icon"></span>
  </div>
  <nav class="main-nav">
    <a class="active">Home</a><a>About Us</a><a>Why QRV</a><a>Our Process</a><a>Client</a><a>Contact Us</a>
  </nav>
</header>

<section class="hero-band"></section>
<div class="hero-slide" role="img" aria-label="Overhead photo of a business team meeting around a conference table with laptops"></div>
<div class="hero-caption">Introducing A Brand-new Way To Manage Your Treasury Management Fees</div>
<div class="slider-dots"><span></span><span class="on"></span><span></span></div>

<h2 class="section-title" style="top:652px">Welcome <em>QRV Consulting</em></h2>
<div class="title-rule" style="top:698px"></div>
<p class="welcome-text">We help large organizations regain control over treasury and banking costs. Our team reviews account analysis statements, benchmarks service fees against the market and negotiates better terms with your banking partners. The result is a clear picture of what you pay, why you pay it and how much can be saved each year. We work alongside your finance staff, keep your existing relationships intact and report every finding in plain language so leaders can act quickly and with confidence, year after year.</p>
<div class="btn" style="left:560px;top:852px;width:80px;height:26px">Read More</div>

<section class="why-band"></section>
<h2 class="section-title" style="top:945px">Why <em>QRV</em>?</h2>
<div class="title-rule" style="top:991px"></div>
<div class="arrow-btn" style="left:76px"><svg width="10" height="10" viewBox="0 0 10 10"><path d="M7 1 3 5l4 4" stroke="#fff" stroke-width="2" fill="none"/></svg></div>
<div class="arrow-btn" style="left:1100px"><svg width="10" height="10" viewBox="0 0 10 10"><path d="M3 1l4 4-4 4" stroke="#fff" stroke-width="2" fill="none"/></svg></div>
<article class="why-card" style="left:132px">
  <div class="why-photo" role="img" aria-label="Close-up of a profit chart printed on paper" style="background:linear-gradient(135deg,#f2f3f5 0%,#c9d0d8 55%,#6f7b8a 100%)"></div>
  <h3>Profitability</h3><div class="bar"></div>
  <p>Clients see lower fees and stronger margins within months, with savings tracked clearly in every report.</p>
</article>
<article class="why-card" style="left:460px">
  <div class="why-photo" role="img" aria-label="Business professionals shaking hands" style="background:linear-gradient(135deg,#3b4656 0%,#8d97a4 45%,#e4e6e8 70%,#4a5564 100%)"></div>
  <h3>Insiders</h3><div class="bar"></div>
  <p>Our team comes from the banking side, so we know how pricing is built and where to improve it.</p>
</article>
<article class="why-card" style="left:788px">
  <div class="why-photo" role="img" aria-label="Hands fitting puzzle pieces together" style="background:linear-gradient(135deg,#dcdcdc 0%,#a9a9a9 50%,#5d5d5d 100%)"></div>
  <h3>Involved</h3><div class="bar"></div>
  <p>We stay close to your finance team from first review to final agreement and keep each step simple.</p>
</article>

<section class="video-band" role="img" aria-label="Video still of colleagues reviewing documents at a desk"></section>
<div class="play"><svg width="22" height="24" viewBox="0 0 22 24"><path d="M4 2l16 10L4 22z" fill="#fff"/></svg></div>
<div class="video-label">Watch our video</div>

<h2 class="section-title" style="top:1695px">Our <em>Process</em></h2>
<div class="title-rule" style="top:1741px"></div>
<div class="step" style="left:150px">
  <div class="step-ring"><svg width="56" height="56" viewBox="0 0 56 56"><circle cx="28" cy="28" r="22" fill="#1d3f7a"/><path d="M28 28V6a22 22 0 0 1 22 22z" fill="#c4161c"/></svg></div>
  <h3>Model</h3>
  <p>Build the fee model<br>Map accounts and services<br>Calculate yearly costs</p>
</div>
<svg class="step-arrow" style="left:400px" width="60" height="30" viewBox="0 0 60 30"><path d="M4 20 Q30 2 52 16" stroke="#bbb" stroke-width="3" fill="none"/><path d="M46 8l8 9-11 3z" fill="#bbb"/></svg>
<div class="step" style="left:475px">
  <div class="step-ring"><svg width="60" height="50" viewBox="0 0 60 50"><path d="M6 25h20M34 25h20" stroke="#1d3f7a" stroke-width="6" stroke-linecap="round"/><path d="M20 17l10 8-10 8M40 17l-10 8 10 8" stroke="#c4161c" stroke-width="5" fill="none" stroke-linejoin="round"/></svg></div>
  <h3>Engage</h3>
  <p>Review terms with banks<br>Discuss new pricing<br>Finalize agreements</p>
</div>
<svg class="step-arrow" style="left:740px" width="60" height="30" viewBox="0 0 60 30"><path d="M4 20 Q30 2 52 16" stroke="#bbb" stroke-width="3" fill="none"/><path d="M46 8l8 9-11 3z" fill="#bbb"/></svg>
<div class="step" style="left:800px">
  <div class="step-ring"><svg width="56" height="56" viewBox="0 0 56 56"><circle cx="23" cy="23" r="15" fill="none" stroke="#1d3f7a" stroke-width="6"/><path d="M34 34l14 14" stroke="#c4161c" stroke-width="7" stroke-linecap="round"/></svg></div>
  <h3>Audit</h3>
  <p>Check pricing each month<br>Confirm savings hold<br>Report results to leaders</p>
</div>

<section class="contact-band"></section>
<h2 class="section-title contact-title" style="top:2100px">Contact <em>Us</em></h2>
<ul class="contact-info">
  <li><svg width="12" height="16" viewBox="0 0 12 16"><path d="M6 0a6 6 0 0 0-6 6c0 4.5 6 10 6 10s6-5.5 6-10a6 6 0 0 0-6-6zm0 8.5A2.5 2.5 0 1 1 6 3.5a2.5 2.5 0 0 1 0 5z" fill="#c4161c"/></svg><span>88 Harbor Point Drive, Suite 400<br>Lakeview, ST 00000</span></li>
  <li><svg width="14" height="12" viewBox="0 0 14 12"><rect x="0.5" y="0.5" width="13" height="11" fill="none" stroke="#c4161c"/><path d="M1 1l6 5 6-5" stroke="#c4161c" fill="none"/></svg><span>Email : info@qrv-consulting.example</span></li>
  <li><svg width="14" height="14" viewBox="0 0 24 24"><path fill="#c4161c" d="M6.6 10.8a15 15 0 0 0 6.6 6.6l2.2-2.2c.3-.3.7-.4 1-.2 1.1.4 2.3.6 3.6.6.6 0 1 .4 1 1V20c0 .6-.4 1-1 1A17 17 0 0 1 3 4c0-.6.4-1 1-1h3.5c.6 0 1 .4 1 1 0 1.3.2 2.5.6 3.6.1.3 0 .7-.2 1z"/></svg><span>Phone : (555) 014-2780</span></li>
</ul>
<form class="contact-form">
  <div class="field">Name</div>
  <div class="field">Email</div>
  <div class="field">Company</div>
  <div class="field msg">Message</div>
  <div class="submit">SUBMIT</div>
</form>

<footer class="site-footer">
  <div class="footer-links">Home | About | Why QRV | Our Process | Client | Contact Us</div>
  <div class="copyright">Copyright © 2024 QRV Consulting . All Rights Reserved.</div>
  <div class="follow">Follow Us : <span class="dot-icon"></span><span class="dot-icon red"></span><span class="dot-icon"></span><span class="dot-icon red"></span><span class="dot-icon"></span></div>
</footer>

</body>
</html>
```